Health Information/Education Logo Design

We need a logo design for a new company based in Atlanta called Brightpath Care. The program is about patient empowerment. We provide health information and education on how to get healthy, stay healthy, and how to be proactive in your care. We also provide medication and injection training to help patients feel their best and to ensure successful therapy outcomes.
We like the colors yellow, pink, teal and purple and would like to see some or all of these colors in the designs. The final design should communicate caring, considerate, compassionate information, education and training services
Education
Contact Information for Business Card
Brightpath Care
Lorraine Pettaway RN, MSN, MHA
Nurse Educator
404.555.0187 cell
404.555.0142 fax

```html
<!DOCTYPE html>
<html lang="en">
<head>
<meta charset="utf-8">
<title>Brightpath Care – Business Card</title>
<link href="https://fonts.googleapis.com/css2?family=Exo+2:wght@400;500&display=swap" rel="stylesheet">
<style>
  :root{
    --backdrop:#8e8f91;
    --card-top:#ffffff;
    --card-bottom:#e6e7e8;
    --brand-teal:#00a9b5;
    --accent-pink:#e8508f;
    --accent-purple:#6b3f8f;
    --ink:#333638;
    --paper:#ffffff;
  }
  *{margin:0;padding:0;box-sizing:border-box}
  html,body{width:1200px;height:894px;overflow:hidden;background:var(--backdrop)}
  body{font-family:"Exo 2",sans-serif;position:relative}
  .card{
    position:absolute;left:150px;top:190px;width:900px;height:514px;
    background:linear-gradient(160deg,var(--card-top) 0%,var(--card-bottom) 100%);
    box-shadow:0 18px 40px rgba(0,0,0,.28);overflow:hidden;
  }
  .brand{
    position:absolute;left:62px;top:62px;
    display:flex;align-items:center;gap:14px;
  }
  .brand__dot{width:18px;height:18px;border-radius:50%;background:var(--accent-pink);flex:none}
  .brand__name{font-size:44px;font-weight:400;color:var(--brand-teal);letter-spacing:1px;line-height:1}
  .band{position:absolute;background:var(--brand-teal)}
  .band--left{left:0;top:148px;width:326px;height:52px}
  .band--right{left:334px;top:172px;right:0;height:118px}
  .band__url{
    position:absolute;right:150px;top:40px;
    color:var(--paper);font-size:24px;letter-spacing:1px;
  }
  .person{position:absolute;right:48px;top:84px;text-align:right}
  .person__name{font-size:24px;color:var(--brand-teal);letter-spacing:1px;line-height:1}
  .person__credentials{font-size:14px;color:var(--accent-purple);letter-spacing:1.5px;margin-top:6px;line-height:1}
  .person__title{font-size:16px;color:var(--ink);letter-spacing:2px;margin-top:6px;line-height:1}
  .contact-list,.social-list{position:absolute;list-style:none}
  .contact-list{left:40px;top:222px}
  .social-list{left:560px;top:378px}
  .contact-list li,.social-list li{
    display:flex;align-items:center;gap:16px;height:36px;
    font-size:16px;color:var(--ink);letter-spacing:.5px;
  }
  .icon-box{
    width:24px;height:24px;background:var(--brand-teal);
    display:flex;align-items:center;justify-content:center;flex:none;
  }
</style>
</head>
<body>
  <div class="card">
    <div class="brand">
      <span class="brand__name">Brightpath Care</span>
      <span class="brand__dot"></span>
    </div>

    <div class="person">
      <div class="person__name">LORRAINE PETTAWAY</div>
      <div class="person__credentials">RN, MSN, MHA</div>
      <div class="person__title">NURSE EDUCATOR</div>
    </div>

    <div class="band band--left"></div>
    <div class="band band--right">
      <span class="band__url">www.brightpathcare.com/123</span>
    </div>

    <ul class="contact-list">
      <li>
        <span class="icon-box">
          <svg width="14" height="14" viewBox="0 0 14 14"><path d="M7 1a4 4 0 0 0-4 4c0 3 4 8 4 8s4-5 4-8a4 4 0 0 0-4-4z" fill="#fff"/><circle cx="7" cy="5" r="1.5" fill="#00a9b5"/></svg>
        </span>
        Peachtree Lane 123
      </li>
      <li>
        <span class="icon-box">
          <svg width="14" height="14" viewBox="0 0 14 14"><path d="M3 1h2.5l1 3-1.5 1a8 8 0 0 0 4 4l1-1.5 3 1V11a2 2 0 0 1-2 2A10 10 0 0 1 1 3a2 2 0 0 1 2-2z" fill="#fff"/></svg>
        </span>
        404.555.0187
      </li>
      <li>
        <span class="icon-box">
          <svg width="14" height="14" viewBox="0 0 14 14"><rect x="1" y="3" width="12" height="8" fill="#fff"/><path d="M1 3l6 4 6-4" fill="none" stroke="#00a9b5" stroke-width="1.2"/></svg>
        </span>
        care@brightpath.com
      </li>
    </ul>

    <ul class="social-list">
      <li><span class="icon-box"></span>www.brightpathcare.com</li>
      <li><span class="icon-box"></span>www.chirpline.com</li>
      <li><span class="icon-box"></span>www.friendwall.com</li>
    </ul>
  </div>
</body>
</html>
```